stars + comments Reviews website design (similar to quarn concept)

Please refer to attached logo and wire frames
----------------------------------------------------------------------------------------------------
we are a company based in egypt, seeking a design for a website that allows user to find doctors using search and filters.
also it allows user to review this doctor through providing comment and 1 to 5 stars
i need 4 main pages designs:
1- Doctors list/favorites list
2- Doctor view
3- Add doctor (3 steps)
4- Sign-in/sign up
5- Menu design
am into the colors teal/turquoise (though am open for different opinion)
i don't want the design theme to be doctors specific
am into the school of very clean, very neat, very simple
(plombex, ruvanteo, melvoshade designs are appealing to me)

Number of Pages Required

4 page

Font styles to use
Sans Serif

Colors
00a990
33b8a4

Requirements
Must have
• website will be bilingual/ bi-directional (English and Arabic)
• designer needs to provide another copy of the design with "right to left" orientation
• interactive button animation

```html
<!DOCTYPE html>
<html lang="en">
<head>
<meta charset="utf-8">
<title>Oplyra – Sign In</title>
<link rel="stylesheet" href="https://fonts.googleapis.com/css2?family=Open+Sans:wght@400;600&family=Poppins:wght@500;600&display=swap">
<style>
  :root {
    --teal: #00989a;
    --teal-dark: #00787a;
    --teal-bright: #16b3b5;
    --footer: #067f85;
    --band: #e4e4e4;
    --page: #fdfdfd;
    --card-border: #dcdcdc;
    --field-border: #c9c9c9;
    --text: #555;
    --heading: #111;
    --icon-muted: #c2c2c2;
    --white: #fff;
  }
  * { box-sizing: border-box; margin: 0; padding: 0; }
  html, body { width: 1200px; height: 625px; overflow: hidden; }
  body {
    position: relative;
    background: var(--page);
    font-family: "Open Sans", Arial, sans-serif;
    color: var(--text);
  }

  .site-header {
    position: absolute; left: 0; top: 0; width: 1200px; height: 62px;
    background: var(--white);
  }
  .brand {
    position: absolute; left: 0; top: 0; width: 330px; height: 62px;
    background: var(--teal);
    clip-path: polygon(0 0, 330px 0, 316px 62px, 0 62px);
    display: flex; align-items: center; padding-left: 30px; gap: 10px;
  }
  .brand-mark { width: 22px; height: 22px; border-radius: 50%; background: var(--white); }
  .brand-name {
    font-family: "Open Sans", Arial, sans-serif; font-weight: 600;
    font-size: 32px; color: var(--white); letter-spacing: 0.2px;
  }
  .main-nav svg { position: absolute; top: 16px; width: 30px; height: 30px; }
  .nav-home { left: 456px; }
  .nav-favorites { left: 601px; }
  .nav-doctors { left: 765px; }
  .utility-nav svg { position: absolute; top: 21px; width: 18px; height: 18px; }
  .nav-settings { left: 1094px; }
  .nav-lock { left: 1122px; }

  .top-band { position: absolute; left: 0; top: 62px; width: 1200px; height: 105px; background: var(--band); }

  .auth-card {
    position: absolute; left: 60px; top: 84px; width: 1080px; height: 468px;
    background: var(--white); border: 1px solid var(--card-border); border-radius: 6px;
  }
  .auth-divider { position: absolute; left: 540px; top: 22px; width: 1px; height: 428px; background: #f0f0f0; }

  .field {
    position: absolute; left: 104px; width: 332px; height: 35px;
    border: 1px solid var(--field-border); border-radius: 3px;
    font-size: 13.5px; color: #666; padding: 0 12px; line-height: 33px;
  }
  .field svg { position: absolute; right: 9px; top: 9px; width: 16px; height: 16px; }
  .field-email { top: 132px; }
  .field-password { top: 181px; }

  .remember {
    position: absolute; left: 104px; top: 231px; font-size: 13.5px; color: #555;
    display: flex; align-items: center; gap: 9px;
  }
  .remember-box { width: 12px; height: 12px; border: 1px solid #999; background: #eee; }

  .btn {
    position: absolute; width: 332px; height: 46px;
    background: var(--teal); border-bottom: 3px solid var(--teal-dark); border-radius: 3px;
    color: var(--white); font-family: "Poppins", Arial, sans-serif; font-weight: 500;
    font-size: 17px; text-align: center; line-height: 45px; letter-spacing: 0.3px;
  }
  .btn-sign-in { left: 104px; top: 270px; }
  .btn-create { left: 644px; top: 235px; }

  .forgot {
    position: absolute; left: 104px; top: 321px; width: 330px; text-align: right;
    font-size: 13.5px; color: var(--teal);
  }
  .signup-title {
    position: absolute; left: 644px; top: 184px; width: 332px; text-align: center;
    font-family: "Poppins", Arial, sans-serif; font-weight: 500; font-size: 18.5px; color: var(--heading);
  }

  .site-footer {
    position: absolute; left: 0; top: 580px; width: 1200px; height: 45px; background: var(--footer);
  }
  .copyright { position: absolute; left: 73px; top: 13px; font-size: 13.5px; color: var(--white); }
  .social { position: absolute; top: 9px; width: 28px; height: 28px; border: 2px solid var(--white); border-radius: 50%; }
  .social-1 { left: 1040px; } .social-2 { left: 1075px; } .social-3 { left: 1110px; }
</style>
</head>
<body>
  <header class="site-header">
    <div class="brand"><span class="brand-mark"></span><span class="brand-name">Oplyra</span></div>
    <nav class="main-nav">
      <svg class="nav-home" viewBox="0 0 30 30" aria-label="Home"><path d="M15 3 L28 15 H24 V27 H18 V20 H12 V27 H6 V15 H2 Z" fill="var(--teal-bright)"/></svg>
      <svg class="nav-favorites" viewBox="0 0 30 30" aria-label="Favorites"><path d="M15 27 C5 19 1 14 1 9 C1 4.5 4.5 2 8 2 C11 2 13.5 4 15 6.5 C16.5 4 19 2 22 2 C25.5 2 29 4.5 29 9 C29 14 25 19 15 27 Z" fill="var(--icon-muted)"/></svg>
      <svg class="nav-doctors" viewBox="0 0 30 30" aria-label="Doctors"><circle cx="15" cy="8" r="6" fill="var(--icon-muted)"/><path d="M4 29 V22 C4 18 8 15 12 15 H18 C22 15 26 18 26 22 V29 Z" fill="var(--icon-muted)"/><path d="M13 16 L15 22 L17 16 Z" fill="var(--white)"/><rect x="19" y="20" width="4" height="4" fill="var(--white)"/></svg>
    </nav>
    <nav class="utility-nav">
      <svg class="nav-settings" viewBox="0 0 20 20" aria-label="Settings"><g fill="var(--icon-muted)"><circle cx="10" cy="10" r="6.5"/><rect x="8" y="0.5" width="4" height="19"/><rect x="0.5" y="8" width="19" height="4"/><rect x="8" y="0.5" width="4" height="19" transform="rotate(45 10 10)"/><rect x="8" y="0.5" width="4" height="19" transform="rotate(-45 10 10)"/></g><circle cx="10" cy="10" r="2.8" fill="var(--white)"/></svg>
      <svg class="nav-lock" viewBox="0 0 20 20" aria-label="Sign in"><path d="M5 9 V6 A5 5 0 0 1 15 6 V9" fill="none" stroke="var(--icon-muted)" stroke-width="2.4"/><rect x="2.5" y="9" width="15" height="11" rx="1" fill="var(--icon-muted)"/></svg>
    </nav>
  </header>

  <div class="top-band"></div>

  <main class="auth-card">
    <section class="sign-in">
      <div class="field field-email">Enter Your Email
        <svg viewBox="0 0 16 16"><path d="M1.5 6.5 L8 2 L14.5 6.5 V14 H1.5 Z M1.5 6.5 L8 10.5 L14.5 6.5" fill="none" stroke="#aaa" stroke-width="1.3"/></svg>
      </div>
      <div class="field field-password">Enter Your Password
        <svg viewBox="0 0 16 16"><circle cx="11.5" cy="4.5" r="3" fill="#aaa"/><path d="M9.5 6.5 L2 14 M3.5 12.5 L5 14 M5 11 L6.5 12.5" stroke="#aaa" stroke-width="1.8" fill="none"/></svg>
      </div>
      <label class="remember"><span class="remember-box"></span>Remember my credentials</label>
      <div class="btn btn-sign-in">SIGN IN</div>
      <div class="forgot">Forgot Your Password</div>
    </section>
    <div class="auth-divider"></div>
    <section class="sign-up">
      <h2 class="signup-title">NO ACCOUNT YET?</h2>
      <div class="btn btn-create">CREATE ACCOUNT</div>
    </section>
  </main>

  <footer class="site-footer">
    <p class="copyright">Copyright © 2015 Oplyra. All Rights Reserved</p>
    <span class="social social-1" role="img" aria-label="ruvanteo"></span>
    <span class="social social-2" role="img" aria-label="plombex"></span>
    <span class="social social-3" role="img" aria-label="melvoshade"></span>
  </footer>
</body>
</html>
```